依頼詳細
いまあるサンプルを春らしく変えて頂いても結構ですし、違うイメージで一から作成して頂いても結構です。このサンプルデザインに特にこだわりがあるわけではありませんので、良いデザインがあればどんどんご提案下さい。

対象が女性の50代~70代になるのでデザインのおしゃれさも大事ですが、シンプルでわかりやすいデザインを希望します。

A3サイズとB4サイズで作成をして下さい。
内容はまったく同じで用紙に合わせてレイアウトを調整して下さい。

真ん中部分の広告商品の商品名や価格はダミーで入れて頂ければ後から私が加筆します。

今後は季節ごとに配色を変えたり、季節感のある物を軽く挿入する程度で、作って頂いたデザインを通年使用していく予定です。

2ヶ月ごとに新聞広告の作成がありますので、今後ともよろしくお願いします。

選択させて頂いた広告の著作権(財産権)等は当方に譲渡をお願いします。フォントや画像素材などを利用する場合は上記利用用途に使用できることを確認し、第三者の知的財産権等に注意して下さい。
記載項目
会期 4月5日(火)~10日(日)

営業時間 10:00~18:00(最終日のみ15:00迄)

会場 アサギリモール一階・北側 SPACEはなゆき 京都市北区雲井南梅枝町38-6

主催 株式会社明葉 京都市北区雲井西竹丘町17-42 tel075-555-0183

2015年4月のサンプルにあるネットショップとブログの案内は省いて下さい。
サイズ
A3
ページ数
片面
希望イメージ
シンプル 複雑
単色 カラフル
暗い 明るい
日常 高級
遊び心 厳粛
未来的 伝統的
女性的 男性的
希望する色
納品ファイル
• 高解像度JPG (.jpg)
• イラストレーター形式 (.ai)
• フォトショップ形式 (.psd)
補足説明
サンプルを添付をさせて頂きます
たくさんのすばらしいデザインを作成して頂き、皆様本当にありがとうございます。

良いデザインばかりなので選定作業が困難を極めています(笑)

採用させて頂いた方はもちろん、それ以外の方も今後ともよろしくお願い申し上げます。

ありがとうございました。
■ 選んだ理由

女性のデザイナーさんらしくやさしさが伝わってきました。

■ 提案者全員のお礼・コメント

皆様本当にありがとうございました。明葉の広告をこんなたくさんの方にデザインしていただきうれしく思います。今後もよろしくお願いします。

```html
<!DOCTYPE html>
<html lang="ja">
<head>
<meta charset="utf-8">
<title>明葉 SPRING SALE 婦人服</title>
<link rel="stylesheet" href="https://fonts.googleapis.com/css2?family=Noto+Serif+JP:wght@700;900&family=Noto+Sans+JP:wght@400;500;700;900&display=swap">
<style>
:root{
  --rose:#e23d74;
  --rose-deep:#c92a60;
  --rose-soft:#f3b6ca;
  --blush:#fbe3ea;
  --band:#e86a8f;
  --ink:#3a2a2e;
  --ink-soft:#6b5a5e;
  --white:#ffffff;
}
*{margin:0;padding:0;box-sizing:border-box}
html,body{width:856px;height:1200px;overflow:hidden;background:var(--white)}
body{font-family:"Noto Sans JP",sans-serif;color:var(--ink);position:relative}
.flyer{position:relative;width:856px;height:1200px;overflow:hidden}

.blossom-backdrop{
  position:absolute;left:0;top:0;width:856px;height:700px;
  background:
    radial-gradient(ellipse at 80% 12%,#f3b3c8 0%,rgba(243,179,200,0) 45%),
    radial-gradient(ellipse at 10% 40%,#f7c9d7 0%,rgba(247,201,215,0) 50%),
    radial-gradient(ellipse at 90% 55%,#f5bfd0 0%,rgba(245,191,208,0) 40%),
    linear-gradient(180deg,#f4c2d2 0%,#fadbe5 55%,#fdf1f5 100%);
}

.brand{position:absolute;left:22px;top:18px;display:flex;flex-direction:column}
.brand-name{font-weight:700;font-size:24px;color:var(--rose);letter-spacing:2px;line-height:1}
.brand-sub{font-size:11px;color:var(--rose);margin-top:4px;letter-spacing:1px}

.title{position:absolute;left:0;top:45px;width:856px;text-align:center;font-family:"Noto Serif JP",serif;font-weight:900;color:var(--rose)}
.title-shop{font-size:168px;line-height:1;letter-spacing:24px;text-shadow:0 0 6px #fff,0 0 14px #fff}
.title-tag{display:flex;justify-content:center;align-items:center;gap:14px;margin-top:6px;font-size:34px;color:var(--rose-deep);letter-spacing:2px}
.title-tag .mark{width:60px;height:60px;border-radius:50%;background:var(--rose);color:var(--white);display:flex;align-items:center;justify-content:center;font-size:34px}
.title-main{font-size:138px;line-height:1;letter-spacing:20px;margin-top:4px;text-shadow:0 0 6px #fff,0 0 14px #fff}

.schedule{position:absolute;left:40px;top:438px;width:776px;display:flex;justify-content:space-between;align-items:center}
.schedule-item{display:flex;align-items:center;gap:10px}
.label{display:inline-flex;align-items:center;justify-content:center;background:var(--rose);color:var(--white);font-weight:700;font-size:16px;border-radius:6px;width:34px;padding:4px 0;writing-mode:vertical-rl;letter-spacing:2px}
.date{font-weight:900;font-size:40px;color:var(--ink);letter-spacing:1px}
.date small{font-size:24px}
.hours{font-weight:900;font-size:30px;line-height:1.1}
.hours small{display:block;font-size:14px;font-weight:500}

.products{position:absolute;left:40px;top:498px;width:776px;display:grid;grid-template-columns:repeat(3,1fr);column-gap:22px;row-gap:10px}
.product{border-bottom:1px dashed var(--rose-soft);padding-bottom:6px}
.product-name{font-size:16px;font-weight:700;line-height:1.25;min-height:40px;display:flex;align-items:flex-end}
.product-name small{font-size:12px;font-weight:500;margin-left:2px}
.product-price{display:flex;align-items:baseline;gap:6px;margin-top:2px;color:var(--rose)}
.product-price .tag{font-size:13px;background:var(--rose);color:var(--white);padding:2px 6px;border-radius:4px;font-weight:700;align-self:center}
.product-price .amount{font-size:36px;font-weight:900;line-height:1}
.product-price .unit{font-size:17px;font-weight:700}

.promo{position:absolute;left:0;top:704px;width:856px;height:190px;background:linear-gradient(180deg,var(--band),var(--rose-deep));text-align:center;color:var(--white)}
.promo-head{font-family:"Noto Serif JP",serif;font-weight:900;font-size:62px;letter-spacing:4px;padding-top:20px;line-height:1.2}
.promo-sub{font-size:28px;font-weight:700;margin-top:6px;line-height:1.3}
.promo-note{font-size:15px;margin-top:8px;color:var(--blush)}

.info{position:absolute;left:36px;top:916px;width:470px}
.info-row{display:flex;gap:14px;margin-bottom:20px}
.venue-floor{font-size:17px;font-weight:700}
.venue-name{font-size:42px;font-weight:900;color:var(--ink);letter-spacing:1px;line-height:1.2}
.addr{font-size:14px;color:var(--ink-soft)}
.org-name{font-size:30px;font-weight:900;line-height:1.2}
.contact{font-size:15px;color:var(--ink-soft)}

.map{position:absolute;left:530px;top:910px;width:296px;height:272px;background:linear-gradient(160deg,#f2eef0,#e3dadf);border:1px solid #d9ccd2}
</style>
</head>
<body>
<main class="flyer">
  <div class="blossom-backdrop" role="img" aria-label="満開の桜の花の写真"></div>

  <div class="brand">
    <span class="brand-name">LUMIERA</span>
    <span class="brand-sub">Meiyo Collection</span>
  </div>

  <h1 class="title">
    <div class="title-shop">明葉</div>
    <div class="title-tag"><span>SPRING</span><span class="mark">の</span><span>SALE</span></div>
    <div class="title-main">婦人服</div>
  </h1>

  <section class="schedule">
    <div class="schedule-item">
      <span class="label">会期</span>
      <span class="date">4月5日<small>(火)</small>~10日<small>(日)</small></span>
    </div>
    <div class="schedule-item">
      <span class="label">時間</span>
      <span class="hours">10:00~18:00<small>(最終日のみ15:00迄)</small></span>
    </div>
  </section>

  <section class="products">
    <div class="product">
      <div class="product-name">シルクスカーフ・<br>ネックカバー</div>
      <div class="product-price"><span class="tag">均一</span><span class="amount">1,000</span><span class="unit">円~</span></div>
    </div>
    <div class="product">
      <div class="product-name">綿・テンセルTシャツ<small>(日本製)</small></div>
      <div class="product-price"><span class="tag">均一</span><span class="amount">2,900</span><span class="unit">円~</span></div>
    </div>
    <div class="product">
      <div class="product-name">チュニック<small>(S~LL)</small></div>
      <div class="product-price"><span class="tag">均一</span><span class="amount">2,900</span><span class="unit">円~</span></div>
    </div>
    <div class="product">
      <div class="product-name">カーディガン<small>(日本製)</small></div>
      <div class="product-price"><span class="tag">均一</span><span class="amount">4,900</span><span class="unit">円~</span></div>
    </div>
    <div class="product">
      <div class="product-name">パンツ<small>(7号~15号)</small></div>
      <div class="product-price"><span class="tag">均一</span><span class="amount">3,900</span><span class="unit">円~</span></div>
    </div>
    <div class="product">
      <div class="product-name">ジャケット<small>(S~LL)</small></div>
      <div class="product-price"><span class="tag">均一</span><span class="amount">5,900</span><span class="unit">円~</span></div>
    </div>
  </section>

  <section class="promo">
    <div class="promo-head">春物・夏物 特別価格!</div>
    <div class="promo-sub">今回もお値打ち品多数!</div>
    <div class="promo-note">品質・価格に自信を持って取り揃えました。ご来場をお待ちしております。</div>
  </section>

  <section class="info">
    <div class="info-row">
      <span class="label">会場</span>
      <div>
        <div class="venue-floor">アサギリモール一階・北側</div>
        <div class="venue-name">SPACEはなゆき</div>
        <div class="addr">京都市北区雲井南梅枝町38-6</div>
      </div>
    </div>
    <div class="info-row">
      <span class="label">主催</span>
      <div>
        <div class="org-name">株式会社明葉</div>
        <div class="addr">京都市北区雲井西竹丘町17-42</div>
        <div class="contact">TEL.075-555-0183 / lumiera-meiyo.jp</div>
      </div>
    </div>
  </section>

  <div class="map" role="img" aria-label="会場周辺の案内地図"></div>
</main>
</body>
</html>
```